Brake Test Training for Coal Mining

We offer Brake Test Training for Coal Mine workers. It's a legislative requirement that workers who are tasked with performing brake testing have certain competencies to do so. We test Light Vehicles and trailers, Heavy Vehicles and Mobile Mining Equipment like Graders, Scrapers and Dump Trucks.

```html
<!DOCTYPE html>
<html lang="en">
<head>
<meta charset="utf-8">
<title>Brake Test Training Billboard</title>
<link rel="stylesheet" href="https://fonts.googleapis.com/css2?family=Bebas+Neue&family=Poppins:wght@400;500;600;700;800&display=swap">
<style>
  :root {
    --navy: #123a66;
    --navy-deep: #0d2c50;
    --yellow: #f9b800;
    --ink: #1d1d1d;
    --white: #ffffff;
    --page: #ffffff;
    --photo-light: #c59a55;
    --photo-dark: #6e5434;
  }
  html, body {
    margin: 0;
    padding: 0;
    width: 832px;
    height: 1200px;
    overflow: hidden;
    background: var(--page);
  }
  .billboard {
    position: absolute;
    left: 16px;
    top: 400px;
    width: 800px;
    height: 401px;
    box-shadow: 0 2px 10px rgba(0,0,0,0.18);
  }
  .billboard svg { display: block; }
  .headline { font-family: "Bebas Neue", "Oswald", sans-serif; fill: var(--white); }
  .body-text { font-family: "Poppins", sans-serif; }
  .tag-label { font-family: "Poppins", sans-serif; font-size: 14px; font-weight: 500; fill: var(--navy-deep); }
</style>
</head>
<body>
<div class="billboard">
  <svg width="800" height="401" viewBox="0 0 800 401" xmlns="http://www.w3.org/2000/svg">
    <defs>
      <linearGradient id="machineTone" x1="0" y1="0" x2="1" y2="1">
        <stop offset="0" stop-color="var(--photo-light)"/>
        <stop offset="1" stop-color="var(--photo-dark)"/>
      </linearGradient>
    </defs>

    <!-- base panels -->
    <rect class="navy-field" x="0" y="0" width="800" height="401" fill="var(--navy)"/>
    <polygon class="yellow-field" points="394,0 800,0 800,401 564,401" fill="var(--yellow)"/>

    <!-- machine photo area -->
    <rect class="machine-photo" role="img" aria-label="Photo of a backhoe loader on a yellow-toned mine site"
          x="522" y="60" width="278" height="320" rx="6" fill="url(#machineTone)" opacity="0.9"/>

    <!-- brand block -->
    <polygon class="brand-panel" points="0,0 231,0 263,85 0,85" fill="var(--white)"/>
    <circle class="brand-dot" cx="40" cy="43" r="14" fill="var(--navy)"/>
    <text class="brand-name body-text" x="62" y="49" font-size="15" font-weight="700" fill="var(--navy)">SOUTHERN PLANT SKILLS</text>

    <!-- headline -->
    <text class="headline" x="27" y="138" font-size="62" textLength="389" lengthAdjust="spacingAndGlyphs">BRAKE TEST TRAINING</text>

    <rect class="audience-box" x="29" y="148" width="386" height="32" fill="var(--ink)"/>
    <text class="audience body-text" x="40" y="173" font-size="28" textLength="364" lengthAdjust="spacingAndGlyphs">
      <tspan fill="var(--white)" font-weight="400">FOR </tspan><tspan fill="var(--yellow)" font-weight="700">COAL MINE WORKERS</tspan>
    </text>

    <text class="intro body-text" font-size="15.5" fill="var(--white)">
      <tspan x="29" y="197" textLength="324" lengthAdjust="spacingAndGlyphs">Workers testing brakes must meet required</tspan>
      <tspan x="29" y="214" textLength="240" lengthAdjust="spacingAndGlyphs">competencies as per legislation</tspan>
    </text>

    <!-- test list -->
    <text class="list-title body-text" x="29" y="243" font-size="21" font-weight="800">
      <tspan fill="var(--white)">WE </tspan><tspan fill="var(--yellow)">TEST</tspan>
    </text>
    <line class="list-rule" x1="129" y1="240" x2="441" y2="240" stroke="var(--white)" stroke-width="0.8" opacity="0.8"/>

    <g class="tick-list body-text" font-size="19" fill="var(--white)">
      <g class="tick"><circle cx="36" cy="264" r="5.5" fill="var(--yellow)"/><path d="M33.3 264 l2 2 l3.4 -3.6" fill="none" stroke="var(--navy)" stroke-width="1.5"/></g>
      <text x="48" y="270" textLength="244" lengthAdjust="spacingAndGlyphs">Light Vehicles and trailers</text>
      <g class="tick"><circle cx="36" cy="289" r="5.5" fill="var(--yellow)"/><path d="M33.3 289 l2 2 l3.4 -3.6" fill="none" stroke="var(--navy)" stroke-width="1.5"/></g>
      <text x="48" y="295" textLength="144" lengthAdjust="spacingAndGlyphs">Heavy Vehicles</text>
      <g class="tick"><circle cx="36" cy="315" r="5.5" fill="var(--yellow)"/><path d="M33.3 315 l2 2 l3.4 -3.6" fill="none" stroke="var(--navy)" stroke-width="1.5"/></g>
      <text x="48" y="321" textLength="277" lengthAdjust="spacingAndGlyphs">Mobile Mining Equipment like</text>
    </g>

    <g class="equipment-tags">
      <rect x="348" y="241" width="91" height="21" rx="2" fill="var(--yellow)"/>
      <text class="tag-label" x="393.5" y="256.5" text-anchor="middle">Graders</text>
      <rect x="348" y="271" width="91" height="21" rx="2" fill="var(--yellow)"/>
      <text class="tag-label" x="393.5" y="286.5" text-anchor="middle">Scrapers</text>
      <rect x="348" y="301" width="124" height="21" rx="2" fill="var(--yellow)"/>
      <text class="tag-label" x="410" y="316.5" text-anchor="middle">Dump Trucks</text>
    </g>

    <!-- contact band -->
    <polygon class="contact-band" points="0,333 499,333 530,401 0,401" fill="var(--white)"/>

    <g class="phone-icon" fill="var(--navy)">
      <path d="M33 348 c-3 2 -3 7 1 13 c4 6 9 9 13 8 l2 -1 l-4 -6 l-3 1.5 c-2 -1 -4 -4 -5 -7 l2.5 -2 l-4 -6.5 z"/>
      <path d="M42 347 a9 9 0 0 1 8 8" fill="none" stroke="var(--navy)" stroke-width="1.8"/>
      <path d="M42 351 a5 5 0 0 1 4 4" fill="none" stroke="var(--navy)" stroke-width="1.8"/>
    </g>
    <text class="phone body-text" x="62" y="370" font-size="26" font-weight="700" fill="var(--ink)" textLength="171" lengthAdjust="spacingAndGlyphs">1300 555 019</text>

    <g class="globe-icon" fill="none" stroke="var(--navy)" stroke-width="1.6">
      <circle cx="255.5" cy="361" r="11.5"/>
      <ellipse cx="255.5" cy="361" rx="5" ry="11.5"/>
      <line x1="244" y1="361" x2="267" y2="361"/>
      <line x1="246" y1="355" x2="265" y2="355"/>
      <line x1="246" y1="367" x2="265" y2="367"/>
    </g>
    <text class="website body-text" x="276" y="369" font-size="26" font-weight="700" fill="var(--ink)" textLength="225" lengthAdjust="spacingAndGlyphs">www.spskills.net.au</text>
  </svg>
</div>
</body>
</html>
```